Unique Business Card Design

Unique Business Card design for our orthotic and prosthetic company. Our logo is on our website, color is light blue. Unique shape (artificial leg shaped, vertical, etc..) preferred. Logo, business name, individual name and basic demographics needed.

Industry/Entity Type

Business

Contact Information for Business Card

Logo, Industry, Phone # Logo, "Prosthetic & Orthotic Services" Place to add individual name and contact info

Colors
cee9f5

Requirements
Must have
• The icon must be there, placement of "Prosthetic & Orthotic Services" can be moved
Nice to have
• Like the mix of light blue, and a little darker blue. One design included the icons from my website which was a nice touch

```html
<!DOCTYPE html>
<html lang="en">
<head>
<meta charset="utf-8">
<title>LimbWell Inc. Business Card</title>
<link rel="stylesheet" href="https://fonts.googleapis.com/css2?family=Montserrat:wght@400;500;600;700&family=Cormorant+Garamond:ital,wght@1,500&display=swap">
<style>
  :root {
    --brand-blue: #1b62b0;
    --deep-blue: #134e93;
    --light-blue: #cee9f5;
    --ink: #1c1c1c;
    --paper: #ffffff;
    --backdrop: #e6e9ed;
  }
  * { box-sizing: border-box; margin: 0; padding: 0; }
  html, body { width: 1200px; height: 900px; overflow: hidden; }
  body {
    background: var(--backdrop);
    font-family: "Montserrat", Arial, sans-serif;
    position: relative;
  }
  .card {
    position: absolute;
    width: 700px;
    height: 400px;
    border-radius: 24px;
    overflow: hidden;
    box-shadow: 0 10px 30px rgba(0,0,0,0.18);
  }

  /* Back side */
  .card-back { left: 120px; top: 45px; background: var(--brand-blue); color: var(--paper); }
  .back-mark {
    position: absolute; left: 60px; top: 120px;
    width: 120px; height: 120px; border-radius: 50%;
    background: var(--paper);
  }
  .back-brand { position: absolute; left: 215px; top: 105px; }
  .brand-name {
    font-weight: 600; font-size: 34px; letter-spacing: 0.5px; line-height: 1;
  }
  .brand-rule { height: 3px; margin-top: 6px; width: 270px; }
  .card-back .brand-rule { background: var(--paper); }
  .tagline {
    font-family: "Cormorant Garamond", Georgia, serif;
    font-style: italic; font-weight: 500; font-size: 22px; margin-top: 4px;
  }
  .service { position: absolute; text-align: center; width: 150px; }
  .service-icon {
    width: 52px; height: 52px; border-radius: 50%; margin: 0 auto 10px;
    background: radial-gradient(circle at 35% 30%, #ffffff, var(--light-blue) 55%, #8fc3e4);
    border: 2px solid rgba(255,255,255,0.7);
  }
  .service-label { font-weight: 600; font-size: 14px; letter-spacing: 0.5px; }
  .service-orthotics { left: 70px; top: 285px; }
  .service-prosthetics { left: 275px; top: 240px; }
  .service-vascular { left: 480px; top: 195px; }

  /* Front side */
  .card-front { left: 380px; top: 470px; background: var(--paper); }
  .front-art { position: absolute; inset: 0; }
  .front-brand { position: absolute; left: 50px; top: 62px; color: var(--brand-blue); }
  .card-front .brand-rule { background: var(--brand-blue); }
  .contact-list { position: absolute; left: 62px; top: 205px; list-style: none; }
  .contact-list li {
    display: flex; align-items: center; gap: 14px;
    font-size: 17px; font-weight: 500; color: var(--ink); height: 27px;
  }
  .contact-list svg { width: 14px; height: 14px; flex: none; }
  .contact-list .web-domain { color: var(--brand-blue); font-weight: 600; }
  .holder { position: absolute; right: 32px; top: 220px; text-align: right; color: var(--paper); }
  .holder-name { font-weight: 700; font-size: 26px; }
  .holder-role { font-size: 16px; margin-top: 4px; }
  .holder-address { font-size: 15px; margin-top: 12px; line-height: 1.35; }
</style>
</head>
<body>

  <section class="card card-back" aria-label="Card back">
    <div class="back-mark"></div>
    <div class="back-brand">
      <div class="brand-name">LIMBWELL INC.</div>
      <div class="brand-rule"></div>
      <div class="tagline">Prosthetic &amp; Orthotic Services</div>
    </div>
    <div class="service service-orthotics">
      <div class="service-icon" role="img" aria-label="Orthotics icon: joint brace"></div>
      <div class="service-label">ORTHOTICS</div>
    </div>
    <div class="service service-prosthetics">
      <div class="service-icon" role="img" aria-label="Prosthetics icon: standing figure"></div>
      <div class="service-label">PROSTHETICS</div>
    </div>
    <div class="service service-vascular">
      <div class="service-icon" role="img" aria-label="Vascular icon: wheelchair user"></div>
      <div class="service-label">VASCULAR</div>
    </div>
  </section>

  <section class="card card-front" aria-label="Card front">
    <svg class="front-art" viewBox="0 0 700 400" width="700" height="400" aria-hidden="true">
      <path d="M0,345 C110,378 230,392 330,368 L300,400 H0 Z" fill="var(--brand-blue)"/>
      <path d="M0,362 C120,392 220,398 300,388 L290,400 H0 Z" fill="var(--ink)"/>
      <path d="M470,0 C430,60 425,120 410,200 C392,300 320,380 150,400" fill="none" stroke="var(--ink)" stroke-width="6"/>
      <path d="M485,0 H700 V400 H160 C330,380 402,300 422,200 C440,110 445,50 485,0 Z" fill="var(--brand-blue)"/>
      <path d="M600,0 H700 V16 H600 Z" fill="var(--ink)"/>
      <circle cx="555" cy="112" r="86" fill="var(--paper)"/>
      <circle cx="555" cy="112" r="78" fill="var(--brand-blue)"/>
    </svg>

    <div class="front-brand">
      <div class="brand-name">LIMBWELL INC.</div>
      <div class="brand-rule"></div>
      <div class="tagline">Prosthetic &amp; Orthotic Services</div>
    </div>

    <ul class="contact-list">
      <li>
        <svg viewBox="0 0 14 14"><rect x="3.5" y="1" width="7" height="12" rx="1.5" fill="none" stroke="var(--brand-blue)" stroke-width="1.6"/></svg>
        845-555-0142
      </li>
      <li>
        <svg viewBox="0 0 14 14"><path d="M3,1.5 L5.5,4 L4.3,5.6 C5.2,7.6 6.4,8.8 8.4,9.7 L10,8.5 L12.5,11 L11,12.8 C6,12 2,8 1.2,3 Z" fill="var(--brand-blue)"/></svg>
        718.555.0170
      </li>
      <li>
        <svg viewBox="0 0 14 14"><rect x="1.5" y="4" width="11" height="8" rx="1.5" fill="var(--brand-blue)"/><rect x="4" y="1.5" width="6" height="3" fill="var(--brand-blue)"/></svg>
        718.555.0139
      </li>
      <li>
        <svg viewBox="0 0 14 14"><rect x="1" y="3" width="12" height="8.5" rx="1" fill="none" stroke="var(--brand-blue)" stroke-width="1.5"/><path d="M1.5,3.5 L7,8 L12.5,3.5" fill="none" stroke="var(--brand-blue)" stroke-width="1.5"/></svg>
        mellison@limbwellinc.com
      </li>
      <li>
        <svg viewBox="0 0 14 14"><circle cx="7" cy="7" r="5.7" fill="none" stroke="var(--brand-blue)" stroke-width="1.4"/><ellipse cx="7" cy="7" rx="2.5" ry="5.7" fill="none" stroke="var(--brand-blue)" stroke-width="1.2"/><path d="M1.3,7 H12.7" stroke="var(--brand-blue)" stroke-width="1.2"/></svg>
        <span>www.<span class="web-domain">limbwellinc</span>.com</span>
      </li>
    </ul>

    <div class="holder">
      <div class="holder-name">Mara Ellison</div>
      <div class="holder-role">Orthotist/Prosthetist</div>
      <div class="holder-address">820 Harbor Ave.<br>Riverton, NY 11000</div>
    </div>
  </section>

</body>
</html>
```